Naturopath needs product label for new essence range

I need a label design for a new range of Essences. The essences resonate with the energetic chakra centres of the body to shift blockages, balance them and lead to transformation and spiritual growth. I have a logo to be used. The name of the essence range is Corvenna which means "to reveal truth or True Nature". The first essence resonates with the Base Chakra and is called "Base" I would like a strong bold red colour to feature in the design. The label size would be about 76mm x 27mm. See below for the required information to be on the label.
Updates

Hi everyone, I'm not sure if it's important to help with the design, but I've just uploaded the logo in several different formats. Thanks for all your submissions. Also please use a deep red colour, the example from the colour wheel is too light. Kind regards, Brent

Target Market(s)

Adults open to alternative therapies and spiritual development

Industry/Entity Type

Product

Colors
eb1f27

Requirements
Must have
• The logo. A deep red colour as the background or part of the background
"Base"
corvennadrops.com.au
Batch
Expiry
Ingredients: vibrational essence of herbs, flowers and crystals, purified water, brandy (approx 12.5% alcohol)
20ml
Dosage: 7 drops once a day

```html
<!DOCTYPE html>
<html lang="en">
<head>
<meta charset="utf-8">
<title>Corvenna Essences – Base</title>
<link rel="stylesheet" href="https://fonts.googleapis.com/css2?family=Arimo:wght@400;700&family=Cinzel:wght@400&display=swap">
<style>
  :root {
    --label-red: #b0101d;
    --label-gold: #d9b840;
    --stripe-top: #f2b233;
    --stripe-bottom: #b5681a;
    --text-light: #ffffff;
    --text-dark: #1a1a1a;
    --leaf-light: #f3f9f6;
    --leaf-mid: #dcefe7;
  }
  * { margin: 0; padding: 0; box-sizing: border-box; }
  html, body { width: 1200px; height: 426px; overflow: hidden; background: #ffffff; }
  .label {
    position: relative;
    width: 1200px;
    height: 426px;
    overflow: hidden;
    font-family: "Arimo", Arial, sans-serif;
  }
  .label__band {
    position: absolute; left: 0; top: 0;
    width: 100%; height: 311px;
    background: var(--label-red);
  }
  .label__stripe {
    position: absolute; left: 0; top: 311px;
    width: 100%; height: 22px;
    background: linear-gradient(to bottom, var(--stripe-top), var(--stripe-bottom));
  }
  .label__foliage {
    position: absolute; left: 0; top: 333px;
    width: 100%; height: 93px;
    background: linear-gradient(100deg, var(--leaf-light), var(--leaf-mid) 50%, var(--leaf-light));
  }
  .heading {
    color: var(--label-gold);
    font-size: 25px;
    font-weight: 400;
  }
  .ingredients {
    position: absolute; left: 26px; top: 72px; width: 360px;
  }
  .ingredients__text {
    color: var(--text-light);
    font-size: 22px;
    line-height: 28px;
    margin-top: 6px;
  }
  .volume {
    position: absolute; left: 26px; top: 250px;
    color: var(--text-light);
    font-size: 22px;
  }
  .brand {
    position: absolute; left: 400px; top: 150px; width: 400px;
    text-align: center;
    font-size: 48px;
    font-weight: 400;
    letter-spacing: 3px;
    color: var(--label-gold);
  }
  .meaning {
    position: absolute; left: 866px; top: 62px; width: 272px;
    font-size: 24px;
    line-height: 28px;
    color: var(--text-light);
    text-align: justify;
  }
  .meaning .heading { font-size: 24px; }
  .dosage {
    position: absolute; left: 866px; top: 170px;
  }
  .dosage__text {
    color: var(--text-light);
    font-size: 24px;
    margin-top: 6px;
  }
  .website {
    position: absolute; left: 41px; top: 365px;
    font-size: 23px;
    color: var(--text-dark);
  }
  .product-name {
    position: absolute; left: 400px; top: 346px; width: 400px;
    text-align: center;
    font-family: "Cinzel", Georgia, serif;
    font-size: 44px;
    font-weight: 400;
    color: var(--text-dark);
  }
  .batch-info {
    position: absolute; left: 986px; top: 341px;
    font-size: 19px;
    line-height: 34px;
    color: var(--text-dark);
  }
</style>
</head>
<body>
<main class="label">
  <div class="label__band"></div>
  <div class="label__stripe"></div>
  <div class="label__foliage" role="img" aria-label="Soft pale green leaf pattern background"></div>

  <section class="ingredients">
    <h2 class="heading">Ingredients:</h2>
    <p class="ingredients__text">Vibrational essence of herbs, flowers and crystals, purified water, brandy (approx 12.5% alcohol)</p>
  </section>
  <p class="volume">20ml</p>

  <p class="brand">Corvenna</p>

  <p class="meaning"><span class="heading">Corvenna:</span> to reveal the truth; the state of not being hidden</p>

  <section class="dosage">
    <h2 class="heading">Dosage:</h2>
    <p class="dosage__text">7 drops once a day</p>
  </section>

  <p class="website">corvennadrops.com.au</p>
  <h1 class="product-name">BASE</h1>
  <div class="batch-info">
    <p>Batch</p>
    <p>Expiry</p>
  </div>
</main>
</body>
</html>
```